Fennick Medical - Flyer

We are a full service pharmacy that specializes in diabetic testing and medications. We research the patient's insurance to maximize their insurance benefit and then deliver the medications monthly directly to the patient's doorstep, for free! We save the patient, time and money every month.
We would love a flyer that we can distribute to Doctor's offices and patients that sum up our pharmacy. Emphasis on saving money, time, and getting the best quality supplies by maximizing their insurance. We want it to be eye catching, clean, and professional.
You can use our logo or feel free to make your own design.
diabetic patients wanting to save money
Insurance

```html
<!DOCTYPE html>
<html lang="en">
<head>
<meta charset="utf-8">
<title>Fennick Medical – Flyer</title>
<link href="https://fonts.googleapis.com/css2?family=Lato:ital,wght@0,400;0,700;0,900;1,700;1,900&display=swap" rel="stylesheet">
<style>
  :root {
    --lime: #a9cc4e;
    --green-text: #6b9a1c;
    --charcoal: #2a2a2a;
    --grey-line: #6f6f6f;
    --white: #ffffff;
    --burst-text: #d8f07a;
  }
  * { margin: 0; padding: 0; box-sizing: border-box; }
  html, body { width: 921px; height: 1200px; overflow: hidden; background: #f2f2f2; }
  body { font-family: "Lato", sans-serif; }
  .flyer { position: relative; width: 921px; height: 1200px; overflow: hidden; background: var(--white); }

  .hero-photo {
    position: absolute; left: 0; top: 0; width: 921px; height: 440px;
    background: linear-gradient(100deg, #e9ecef 0%, #f7f7f7 30%, #e4e2df 55%, #f3efe9 75%, #dfe3e6 100%);
  }
  .shapes { position: absolute; left: 0; top: 0; width: 921px; height: 1200px; pointer-events: none; }

  .accent-band { position: absolute; left: 0; top: 440px; width: 921px; height: 38px; background: var(--lime); }

  .brand-band { position: absolute; left: 0; top: 478px; width: 921px; height: 145px; background: var(--white); }
  .brand-name {
    position: absolute; left: 36px; top: 52px;
    display: flex; align-items: center; gap: 12px;
    font-weight: 700; font-size: 30px; letter-spacing: 1px; color: var(--charcoal);
    white-space: nowrap;
  }
  .brand-mark { width: 28px; height: 28px; background: var(--lime); }
  .brand-tagline {
    position: absolute; right: 150px; top: 42px; text-align: right;
    font-weight: 700; font-size: 27px; line-height: 1.55; color: var(--green-text);
    white-space: nowrap;
  }

  .offer-panel {
    position: absolute; left: 0; top: 623px; width: 921px; height: 443px;
    background: radial-gradient(ellipse at 48% 35%, #eef9b8 0%, #c9e46e 45%, #a2c443 85%, #98ba3b 100%);
  }
  .offer-heading {
    position: absolute; left: 36px; top: 24px; width: 760px;
    font-weight: 700; font-size: 36px; line-height: 1.3; color: var(--charcoal);
  }
  .offer-body {
    position: absolute; left: 36px; top: 124px; width: 830px;
    font-weight: 700; font-size: 16px; line-height: 1.6; color: var(--charcoal);
  }
  .delivery-box {
    position: absolute; left: 28px; top: 237px; width: 672px; height: 112px;
    border-radius: 10px;
    background: linear-gradient(90deg, #ffffff 0%, #f3f3f3 60%, #d9d9d9 100%);
    box-shadow: 0 3px 6px rgba(0,0,0,0.35);
    padding: 16px 0 0 50px;
    font-weight: 700; font-size: 31px; line-height: 1.3; color: var(--green-text);
  }
  .free-burst { position: absolute; left: 668px; top: 188px; width: 224px; height: 224px; }
  .free-burst span {
    position: absolute; left: 0; top: 48px; width: 100%; text-align: center;
    font-weight: 900; font-style: italic; font-size: 50px; line-height: 0.95; color: var(--burst-text);
    transform: rotate(-6deg);
  }
  .contact-row { position: absolute; left: 28px; top: 382px; width: 620px; height: 44px; }
  .contact-item {
    position: absolute; top: 0; display: flex; align-items: center; gap: 12px;
    font-weight: 700; font-size: 30px; color: var(--charcoal); white-space: nowrap;
  }
  .contact-phone { left: 50px; }
  .contact-email { left: 404px; }

  .footer-rule { position: absolute; left: 0; top: 1066px; width: 921px; height: 19px; background: var(--charcoal); }
  .footer-band { position: absolute; left: 0; top: 1085px; width: 921px; height: 115px; background: var(--lime); }
  .footer-line {
    position: absolute; left: 0; top: 30px; width: 830px; text-align: center;
    font-weight: 700; font-style: italic; font-size: 33px; color: var(--white);
    text-shadow: 0 2px 3px rgba(0,0,0,0.45);
  }
</style>
</head>
<body>
<main class="flyer">
  <div class="hero-photo" role="img" aria-label="Pharmacists in white coats standing in front of stocked pharmacy shelves"></div>

  <div class="accent-band"></div>

  <section class="brand-band">
    <div class="brand-name"><span class="brand-mark"></span>FENNICK MEDICAL</div>
    <p class="brand-tagline">Get the best quality supplies<br>by maximiz insurance</p>
  </section>

  <section class="offer-panel">
    <h1 class="offer-heading">We research the patient's insurance to maximize their insurance benefit</h1>
    <p class="offer-body">Lorem ipsum dolor sit amet, consectetur adipisicing elit, sed do eiusmod tempor incididunt ut labore et dolore magna aliqua. Ut enim ad minim veniam, quis nostrud exercitation proident, sunt in culpa qui officia deserunt mollit anim id est laborum.</p>
    <p class="delivery-box">We deliver the medications monthly<br>directly to the patient's doorstep,</p>
    <div class="free-burst">
      <svg width="224" height="224" viewBox="0 0 230 230" aria-hidden="true">
        <g fill="#1e1e1e" transform="translate(115 115)">
          <rect x="-80" y="-80" width="160" height="160"/>
          <rect x="-80" y="-80" width="160" height="160" transform="rotate(15)"/>
          <rect x="-80" y="-80" width="160" height="160" transform="rotate(30)"/>
          <rect x="-80" y="-80" width="160" height="160" transform="rotate(45)"/>
          <rect x="-80" y="-80" width="160" height="160" transform="rotate(60)"/>
          <rect x="-80" y="-80" width="160" height="160" transform="rotate(75)"/>
        </g>
      </svg>
      <span>for<br>free!</span>
    </div>
    <div class="contact-row">
      <div class="contact-item contact-phone">
        <svg width="34" height="38" viewBox="0 0 34 38" aria-hidden="true">
          <rect width="34" height="38" rx="5" fill="#2a2a2a"/>
          <path d="M11 8 l5 0 l2 7 l-3 2 q2 5 6 8 l3-2 l6 3 l0 5 q-12 1 -19-17 z" fill="#c9e46e"/>
        </svg>
        <span>555-0142-88</span>
      </div>
      <div class="contact-item contact-email">
        <svg width="42" height="28" viewBox="0 0 42 28" aria-hidden="true">
          <rect x="1.5" y="1.5" width="39" height="25" fill="none" stroke="#2a2a2a" stroke-width="3"/>
          <path d="M2 2 L21 16 L40 2 M2 26 L16 12 M40 26 L26 12" fill="none" stroke="#2a2a2a" stroke-width="3"/>
        </svg>
        <span>hi@fennick.com</span>
      </div>
    </div>
  </section>

  <div class="footer-rule"></div>
  <footer class="footer-band">
    <p class="footer-line">We save the patient, time and money every month</p>
  </footer>

  <svg class="shapes" viewBox="0 0 921 1200" aria-hidden="true">
    <polygon points="0,0 300,0 150,120 0,68" fill="#a9cc4e"/>
    <polygon points="0,68 150,120 300,0 330,0 160,140 0,92" fill="#6f6f6f"/>
    <polygon points="921,270 712,430 921,500" fill="#a9cc4e"/>
    <line x1="712" y1="430" x2="921" y2="505" stroke="#2a2a2a" stroke-width="5"/>
    <polygon points="720,440 921,440 921,478 830,478" fill="#ffffff"/>
    <polygon points="700,623 921,623 921,718" fill="#ffffff"/>
    <line x1="700" y1="622" x2="921" y2="718" stroke="#2a2a2a" stroke-width="4"/>
    <polygon points="830,1066 921,1066 921,1165" fill="#2a2a2a"/>
  </svg>
</main>
</body>
</html>
```